Larkspur Elementary
Stationary, Letterhead, Business Card
Simple
Cora P. Wendt
Counselor
742 Ridgeway Lane
Hollowmere, CO 80999
wendt_cora@mbxsd.org
http://les.hollowmere.k12.xx.us
I would like to stay with the navy gold and blue theme (but variations are fine) but a white background is not necessary.
I like the vertical look more than the horizontal but both are welcomed.
If you follow the link, I like how #8, #15, and #18 look format-wise.
I look forward to your designs.
http://www.quarvelblog.com/2008/06/25/yet-another-post-with-unique-business-cards/
Logo plus your creative touches

```html
<!DOCTYPE html>
<html lang="en">
<head>
<meta charset="utf-8">
<title>Larkspur Elementary – Stationery</title>
<link href="https://fonts.googleapis.com/css2?family=Oswald:wght@600&family=Open+Sans:wght@400;600;700&display=swap" rel="stylesheet">
<style>
:root{
  --stage:#e8e8e8;
  --paper:#ffffff;
  --navy:#1d3f7a;
  --blue:#2d6db5;
  --gold:#d49a1e;
  --charcoal:#2f2f31;
  --charcoal-deep:#1f1f21;
  --ink:#4a4a4a;
  --muted:#8a8a8a;
  --faint:#eef0f3;
}
*{box-sizing:border-box;margin:0;padding:0}
html,body{width:1200px;height:840px;overflow:hidden}
body{background:var(--stage);font-family:"Open Sans",sans-serif;color:var(--ink);position:relative}
.brand{display:flex;align-items:center;gap:8px}
.brand-mark{width:22px;height:22px;background:var(--gold);flex:none}
.brand-name{font-family:"Oswald",sans-serif;font-weight:600;text-transform:uppercase;color:var(--navy);line-height:1}

/* Letterhead */
.letterhead{position:absolute;left:14px;top:24px;width:460px;height:590px;background:var(--paper);box-shadow:0 2px 8px rgba(0,0,0,.18);padding:26px 30px;overflow:hidden}
.letterhead .brand-name{font-size:21px}
.letterhead-top{display:flex;justify-content:space-between;align-items:flex-start}
.contact-list{list-style:none;font-size:6.5px;line-height:11px;color:var(--muted)}
.contact-list li::before{content:"";display:inline-block;width:5px;height:5px;background:var(--blue);margin-right:5px;vertical-align:middle}
.letter-body{margin-top:30px;font-size:6.4px;line-height:9.6px;text-align:justify}
.letter-body p{margin-bottom:12px}
.letter-body .source{display:block;color:var(--muted)}
.signature{width:70px;height:16px;background:linear-gradient(90deg,#c9d3e4,#e6ebf3);margin:4px 0 3px}
.letter-art{position:absolute;right:-20px;bottom:30px;width:230px;height:200px;background:radial-gradient(ellipse at 60% 60%,#e4e8ee 0%,rgba(255,255,255,0) 70%)}
.letter-url{position:absolute;left:0;right:0;bottom:14px;text-align:center;font-size:7px;color:var(--muted)}

/* Envelope */
.envelope{position:absolute;left:497px;top:24px;width:690px;height:312px;background:var(--paper);box-shadow:0 2px 8px rgba(0,0,0,.18);overflow:hidden}
.envelope-flap{position:absolute;inset:0}
.envelope-art{position:absolute;left:20px;top:150px;width:280px;height:150px;background:radial-gradient(ellipse at 50% 50%,#e6e9ee 0%,rgba(255,255,255,0) 70%)}
.envelope .brand{position:absolute;left:300px;top:170px}
.envelope .brand-name{font-size:26px}
.envelope .brand-mark{width:30px;height:30px}
.envelope-return{position:absolute;left:88px;top:245px;font-size:7px;color:var(--muted)}

/* Business cards */
.card{position:absolute;background:linear-gradient(145deg,var(--charcoal),var(--charcoal-deep));box-shadow:0 3px 9px rgba(0,0,0,.3);overflow:hidden;color:#d9d9d9}
.card-front{left:617px;top:480px;width:248px;height:216px;padding:22px 18px}
.card-art{position:absolute;right:-10px;bottom:-10px;width:150px;height:140px;background:radial-gradient(ellipse at 55% 55%,#45464a 0%,rgba(47,47,49,0) 70%)}
.name-bar{background:var(--gold);color:#fff;font-weight:700;font-size:10px;letter-spacing:.5px;padding:3px 8px;display:inline-block;margin-left:70px;text-transform:uppercase}
.role{font-size:7px;color:#bdbdbd;margin:3px 0 0 78px}
.card-contact{list-style:none;font-size:6.6px;line-height:11px;margin-top:40px;position:relative}
.card-url{position:absolute;left:18px;bottom:12px;font-size:6.5px;color:#9a9a9a}
.card-back{left:900px;top:425px;width:288px;height:295px}
.card-back-art{position:absolute;inset:0;background:radial-gradient(ellipse at 45% 45%,#48494d 0%,rgba(47,47,49,0) 65%)}
.card-back .brand{position:absolute;left:50px;top:120px}
.card-back .brand-name{color:#fff;font-size:22px}
.card-back .card-url{left:0;right:0;text-align:center;bottom:16px;font-size:8px}
</style>
</head>
<body>

<section class="letterhead">
  <div class="letterhead-top">
    <div class="brand"><span class="brand-mark"></span><span class="brand-name">Larkspur Elementary</span></div>
    <ul class="contact-list">
      <li>742 Ridgeway Lane, Hollowmere, CO 80999</li>
      <li>303.555.0142</li>
      <li>303.555.0143</li>
      <li>wendt_cora@mbxsd.org</li>
    </ul>
  </div>
  <div class="letter-body">
    <p>Dear,<br>Someone Somebody</p>
    <p>We are glad to welcome every family to a new school year. Our counseling team works with students, parents and teachers to build a safe and caring place to learn. Each child brings unique strengths, and we aim to help them grow with confidence, kindness and a strong sense of belonging in every classroom and hallway of our school community.<span class="source">Section 2.14 of the Family Guide, written by Varro Quill in 2011</span></p>
    <p>Throughout the year we offer small groups, classroom lessons and individual meetings. Topics include friendship, handling worry, setting goals and solving problems together. Parents are always welcome to call or stop by the office to share questions or concerns. Working as partners, we can give each student the support needed to succeed both in school and beyond, today and for many years ahead.<span class="source">Revised edition by H. Dellmore</span></p>
    <p>Please watch for our monthly newsletter, which lists upcoming events, helpful reading and simple ideas to try at home. We also keep a lending shelf of books about feelings and family change. If you would like to join our parent circle, reply to this letter or email the office. Thank you for trusting us with your children, and we look forward to a wonderful year together with all of you.<span class="source">Section 3.02 of the Family Guide, written by Varro Quill in 2011</span></p>
    <p>Yours Truly,<br>Revised edition by H. Dellmore</p>
    <div class="signature" role="img" aria-label="Handwritten signature"></div>
    <p>H. Dellmore</p>
  </div>
  <div class="letter-art" role="img" aria-label="Faint scattered puzzle piece decoration"></div>
  <div class="letter-url">http://les.hollowmere.k12.xx.us</div>
</section>

<section class="envelope">
  <svg class="envelope-flap" width="690" height="312" viewBox="0 0 690 312" aria-hidden="true">
    <defs>
      <linearGradient id="flapShade" x1="0" y1="0" x2="0" y2="1">
        <stop offset="0" stop-color="#3a3a3c"/>
        <stop offset="1" stop-color="#1f1f21"/>
      </linearGradient>
    </defs>
    <polygon points="0,0 690,0 690,40 345,145 0,40" fill="url(#flapShade)"/>
  </svg>
  <div class="envelope-art" role="img" aria-label="Faint scattered puzzle piece decoration"></div>
  <div class="brand"><span class="brand-mark"></span><span class="brand-name">Larkspur Elementary</span></div>
  <div class="envelope-return">742 Ridgeway Lane, Hollowmere, CO 80999</div>
</section>

<section class="card card-front">
  <div class="card-art" role="img" aria-label="Faint puzzle piece decoration"></div>
  <div class="name-bar">Cora P. Wendt</div>
  <div class="role">Counselor</div>
  <ul class="card-contact">
    <li>742 Ridgeway Lane</li>
    <li>Hollowmere, CO 80999</li>
    <li>303.555.0142</li>
    <li>wendt_cora@mbxsd.org</li>
  </ul>
  <div class="card-url">http://les.hollowmere.k12.xx.us</div>
</section>

<section class="card card-back">
  <div class="card-back-art" role="img" aria-label="Faint puzzle piece decoration"></div>
  <div class="brand"><span class="brand-mark"></span><span class="brand-name">Larkspur Elementary</span></div>
  <div class="card-url">http://les.hollowmere.k12.xx.us</div>
</section>

</body>
</html>
```